Design Project - Finance Website (Only need PSD)

UPDATED PROJECT (Now only PSD needed)
Need a Wordpress design for a company called "Harrowgate Capital Finance". The company provides finance for corporate clients, businesses and property developers. The design should be business like with appealing colours that communicate trust. I have uploaded a banner and logo to be incorporated or feel free to design something better if you think you can.
** I now only need the PSD
** I want something that is actually designed rather than from a template.
Thanks
Updates
The website will be used for lead generation so the contact form with adjustable fields in the Wordpress backend should be fairly prominent on the page.
I have uploaded a banner and logo for the site. None of the designs I have seen so far were good enough so the first decent design using the new banner and logo provided will win the job. I do not want just a template that has been cut and paste from somewhere else, I want decent design. If anyone provides a decent design then I will give an extra bonus of $150.
Reason: I have uploaded a banner and logo for the site. None of the designs I have seen so far were good enough so the first decent design using the new banner and logo provided will win the job. I do not want just a template that has been cut and paste from somewhere else, I want decent design. If anyone provides a decent design then I will give an extra bonus of $150.
Thanks
Target Market(s)
Business owners & property developers
Industry/Entity Type
Finance
Requirements
Must have
- Contact form on home page that can be altered through the back end eg. ability to add or remove fields. Widgetised sidebars.
Nice to have
- Widgetised footer.

```html
<!DOCTYPE html>
<html lang="en">
<head>
<meta charset="utf-8">
<title>Harrowgate Capital Finance</title>
<link href="https://fonts.googleapis.com/css2?family=Yanone+Kaffeesatz:wght@400;500&family=Arimo:wght@400;700&family=Open+Sans:wght@400&display=swap" rel="stylesheet">
<style>
:root{
  --blue:#3a7bd0;
  --blue-dark:#2a5d9c;
  --blue-head:#3566a6;
  --green:#9cc43e;
  --green-light:#b8d96a;
  --text:#555;
  --dark:#333;
  --panel:#efefef;
  --field:#e6e6e6;
  --footer:#434343;
  --footer-text:#f2f2f2;
}
*{margin:0;padding:0;box-sizing:border-box}
html,body{width:1074px;height:1200px;overflow:hidden;background:#fff}
body{position:relative;font-family:"Arimo",Arial,sans-serif;color:var(--text)}
.abs{position:absolute}
.brand{left:80px;top:30px;display:flex;align-items:center;gap:10px;font-family:"Arimo",Arial,sans-serif;font-size:21px;letter-spacing:3px;color:var(--blue-dark);text-transform:uppercase}
.brand-mark{width:24px;height:24px;background:var(--blue-dark)}
.search{left:666px;top:36px;width:187px;height:28px;background:#eee;border:1px solid #ddd}
.search-btn{left:855px;top:36px;width:28px;height:28px;background:var(--green);display:flex;align-items:center;justify-content:center}
.social{top:23px;width:42px;height:42px;border-radius:4px}
.social.one{left:898px;background:#3b5998}
.social.two{left:954px;background:#56b3d9}
.nav{left:79px;top:84px;width:916px;height:35px;background:linear-gradient(#b7d870,#97c045);border-radius:8px 8px 0 0;display:flex;font-family:"Yanone Kaffeesatz",sans-serif;font-size:19px;color:#fff;text-transform:uppercase}
.nav a{color:#fff;text-decoration:none;display:flex;align-items:center;justify-content:center;border-left:1px solid rgba(255,255,255,.35)}
.nav a.active{background:linear-gradient(#5d9be3,#3a7bd0);border-radius:8px 0 0 0;border:none}
.hero{left:0;top:119px;width:1074px;height:317px;background:linear-gradient(90deg,#4a8ae0,#3b7ccf 60%,#4a8ae0)}
.hero-photo{left:474px;top:119px;width:521px;height:317px;background:linear-gradient(180deg,#c9dff2 0%,#8fa9c0 45%,#5e7c8f 75%,#5f9a3c 100%)}
.points{left:80px;top:242px;list-style:none;font-family:"Open Sans",sans-serif;font-size:20px;color:#fff}
.points li{display:flex;align-items:center;gap:14px;height:32.5px}
.dots{left:80px;top:403px;display:flex;gap:9px}
.dots span{width:14px;height:14px;border-radius:50%;background:#9cc0ee}
.dots span:first-child{background:#fff}
.welcome{left:81px;top:455px;font-family:"Yanone Kaffeesatz",sans-serif;font-weight:500;color:#222;font-size:21px;text-transform:uppercase}
.welcome b{color:var(--blue-head);font-size:32px;font-weight:500}
.intro{left:82px;top:502px;width:914px;font-size:12.5px;line-height:21.5px;text-align:justify}
.btn{background:var(--dark);color:#fff;font-family:"Arimo",sans-serif;font-weight:700;font-size:16px;border-radius:10px;display:flex;align-items:center;justify-content:center}
.panel{left:79px;top:672px;width:916px;height:326px;background:var(--panel);border:1px solid #e2e2e2;border-radius:8px}
.card{top:692px;width:282px;height:287px;background:#fff;border-radius:8px}
.card h2{position:absolute;left:20px;top:14px;font-family:"Yanone Kaffeesatz",sans-serif;font-weight:500;font-size:32px;color:var(--blue-head);text-transform:uppercase}
.thumb{width:59px;height:63px;border:1px solid #ddd;background:linear-gradient(#e9e6e3,#c9b7a4)}
.news-item{position:absolute;left:23px;display:flex;gap:14px;font-size:12.3px;line-height:16.5px;text-align:justify}
.news-item p{width:170px}
.field{position:absolute;left:33px;width:240px;height:23px;background:var(--field);border:1px solid #d6d6d6;font-size:12.5px;padding:4px 9px;color:#555}
.footer{left:0;top:1018px;width:1074px;height:182px;background:var(--footer);border-top:2px solid #5a87c4}
.links{top:1042px;list-style:none;font-family:"Open Sans",sans-serif;font-size:12px;color:var(--footer-text);line-height:21.5px}
.foot-brand{left:760px;top:1050px;font-size:16px;letter-spacing:2.5px;color:#ddd;text-transform:uppercase}
.copy{left:852px;top:1087px;font-family:"Open Sans",sans-serif;font-size:10.5px;color:#ccc}
</style>
</head>
<body>
<header>
  <div class="abs brand"><span class="brand-mark"></span>Harrowgate Capital Finance</div>
  <div class="abs search"></div>
  <div class="abs search-btn"><svg width="10" height="10" viewBox="0 0 10 10"><circle cx="4" cy="4" r="3" fill="none" stroke="#fff" stroke-width="1.5"/><line x1="6" y1="6" x2="9" y2="9" stroke="#fff" stroke-width="1.5"/></svg></div>
  <div class="abs social one" role="img" aria-label="Social network link"></div>
  <div class="abs social two" role="img" aria-label="Social network link"></div>
  <nav class="abs nav">
    <a class="active" style="width:127px">Home</a>
    <a style="width:157px">About Us</a>
    <a style="width:157px">Services</a>
    <a style="width:157px">Finance</a>
    <a style="width:165px">Real Estate</a>
    <a style="width:153px">Contact Us</a>
  </nav>
</header>

<section>
  <div class="abs hero"></div>
  <div class="abs hero-photo" role="img" aria-label="Modern glass office building under a blue sky"></div>
  <ul class="abs points">
    <li><svg width="18" height="14" viewBox="0 0 18 14"><path d="M1 7l5 5L17 1" fill="none" stroke="#8cc63f" stroke-width="3"/></svg>Compare several capital provider rates</li>
    <li><svg width="18" height="14" viewBox="0 0 18 14"><path d="M1 7l5 5L17 1" fill="none" stroke="#8cc63f" stroke-width="3"/></svg>Access to real estate and hedge funds</li>
    <li><svg width="18" height="14" viewBox="0 0 18 14"><path d="M1 7l5 5L17 1" fill="none" stroke="#8cc63f" stroke-width="3"/></svg>Optimise your capital returns</li>
  </ul>
  <div class="abs dots"><span></span><span></span><span></span></div>
</section>

<section>
  <h1 class="abs welcome"><b>Welcome</b> to Harrowgate Capital Finance</h1>
  <p class="abs intro">Sed ut perspiciatis unde omnis iste natus error sit voluptatem accusantium doloremque laudantium, totam rem aperiam, eaque ipsa quae ab illo inventore veritatis et quasi architecto beatae vitae dicta sunt explicabo. Nemo enim ipsam voluptatem quia voluptas sit aspernatur aut odit aut fugit, sed quia consequuntur magni dolores eos qui ratione voluptatem sequi nesciunt. Nemo enim ipsam voluptatem quia voluptas sit aspernatur aut odit aut fugit, sed quia consequuntur magni dolores eos qui ratione voluptatem sequi nesciunt. Sed ut perspiciatis unde omnis iste natus error sit voluptatem accusantium doloremque laudantium, totam rem aperiam, eaque ipsa quae ab illo inventore veritatis et quasi architecto beatae vitae dicta sunt explicabo. Nemo enim ipsam voluptatem quia voluptas sit aspernatur aut odit aut fugitincidunt.</p>
  <div class="abs btn" style="left:917px;top:614px;width:78px;height:29px">More</div>
</section>

<section>
  <div class="abs panel"></div>

  <article class="abs card" style="left:96px">
    <h2>Latest News</h2>
    <svg class="abs" style="left:218px;top:22px" width="50" height="22" viewBox="0 0 50 22"><path d="M18 2L6 11l12 9M14 2L2 11l12 9" fill="none" stroke="#5b8fcf" stroke-width="1.5"/><path d="M32 2l12 9-12 9M36 2l12 9-12 9" fill="none" stroke="#5b8fcf" stroke-width="1.5"/></svg>
    <div class="news-item" style="top:63px"><div class="thumb" role="img" aria-label="Author portrait"></div><p>Sed ut perspiciatis unde omnis iste natus error sit voluptatem accusantium doloremque...</p></div>
    <div class="news-item" style="top:139px"><div class="thumb" role="img" aria-label="Author portrait"></div><p>Sed ut perspiciatis unde omnis iste natus error sit voluptatem accusantium doloremque...</p></div>
    <div class="news-item" style="top:211px"><div class="thumb" role="img" aria-label="Author portrait"></div><p>Sed ut perspiciatis unde omnis iste natus error sit voluptatem accusantium doloremque...</p></div>
  </article>

  <article class="abs card" style="left:397px">
    <h2>Case Study</h2>
    <div class="news-item" style="top:63px;left:26px"><div class="thumb" style="width:76px;height:80px" role="img" aria-label="Client portrait"></div><p style="width:152px">Sed ut perspiciatis ref ben unde omnis iste natus error sit voluptatem accusantium doloremque natus error sit voluptatem accusantium ...</p></div>
    <p class="abs" style="left:26px;top:162px;width:245px;font-size:12px;line-height:16.5px">Lorem Ipsum is simply dummy text of the printing and typesetting industry.</p>
    <div class="abs btn" style="left:191px;top:233px;width:79px;height:29px">More</div>
  </article>

  <article class="abs card" style="left:698px">
    <h2 style="left:31px">Contact</h2>
    <div class="field" style="top:65px">Name</div>
    <div class="field" style="top:102px">Email</div>
    <div class="field" style="top:142px"></div>
    <div class="abs" style="left:33px;top:184px;display:flex;align-items:center;gap:8px;font-size:12.5px"><span style="width:12px;height:12px;border:1px solid #bbb;background:#fff"></span>Subscibe to Our Newsletter</div>
    <div class="abs btn" style="left:186px;top:233px;width:81px;height:29px">Submit</div>
  </article>
</section>

<footer>
  <div class="abs footer"></div>
  <ul class="abs links" style="left:80px"><li>Home</li><li>About Us</li><li>Services</li><li>Real Estate</li><li>Contact Us</li></ul>
  <ul class="abs links" style="left:205px"><li>Home</li><li>About Us</li><li>Services</li><li>Real Estate</li><li>Contact Us</li></ul>
  <ul class="abs links" style="left:330px"><li>Home</li><li>About Us</li><li>Services</li><li>Real Estate</li><li>Contact Us</li></ul>
  <ul class="abs links" style="left:466px"><li>Home</li><li>About Us</li><li>Services</li><li>Real Estate</li><li>Contact Us</li></ul>
  <div class="abs foot-brand">Harrowgate Capital Finance</div>
  <div class="abs copy">© 2012. ALL RIGHTS RESERVED</div>
</footer>
</body>
</html>
```